Marcelo Vantrini
Tenor & Vocal Coach
mvbaritono@quellmail.net
(713) 562-8307
www.voicefromthecore.net
Want two sided postcard / rack card.4" x 9"
Front - vertical - picture in t-shirt, name, title (Tenor & Vocal Coach), contact information
Back - horizontal - picture in jacket, name, title (Tenor & Vocal Coach), contact information, bio (see attachment for words)
Do not leave space for an address.
Looking for an edgy modern design!

Target Market(s)

Young adults

Requirements
Nice to have
• Will pay extra to get a complimentary business card design, two sided

```html
<!DOCTYPE html>
<html lang="en">
<head>
<meta charset="utf-8">
<title>Marcelo Vantrini – Tenor &amp; Vocal Coach cards</title>
<link rel="stylesheet" href="https://fonts.googleapis.com/css2?family=Montserrat:wght@600;700&family=Open+Sans:wght@400&family=Oswald:wght@300;400;600&display=swap">
<style>
  :root {
    --navy: #4b5182;
    --navy-deep: #2f3563;
    --tan: #b8ac6c;
    --cream: #ece9df;
    --grey: #85868b;
    --grey-shadow: #62646e;
    --white: #ffffff;
    --ink: #2c3266;
    --page: #eeebe4;
  }
  * { margin: 0; padding: 0; box-sizing: border-box; }
  html, body { width: 1200px; height: 330px; overflow: hidden; }
  body { background: var(--page); position: relative; }

  .card {
    position: absolute;
    top: 47px;
    width: 540px;
    height: 240px;
    background: var(--navy);
    overflow: hidden;
  }
  .card--front { left: 42px; }
  .card--back { left: 619px; }

  .card__shapes { position: absolute; inset: 0; width: 540px; height: 240px; }

  .photo {
    position: absolute;
    top: 0;
    height: 240px;
  }
  .card--front .photo {
    left: 184px; width: 179px;
    background: radial-gradient(ellipse at 55% 40%, #f1ede4 0%, #d9d4c8 45%, #a9a79f 100%);
  }
  .card--back .photo {
    left: 81px; width: 213px;
    background: linear-gradient(180deg, #e0d3bf 0%, #cbb9a0 45%, #5a5f7c 80%, #2f3450 100%);
  }

  .frame {
    position: absolute;
    left: 15px; top: 8px;
    width: 510px; height: 225px;
    border: 1.5px solid rgba(255,255,255,0.75);
  }

  .identity {
    position: absolute;
    left: 45px; top: 106px;
    color: var(--ink);
  }
  .identity__name {
    font-family: "Montserrat", sans-serif;
    font-weight: 700;
    font-size: 12px;
    font-variant: small-caps;
    letter-spacing: 0.6px;
  }
  .identity__title {
    font-family: "Open Sans", sans-serif;
    font-size: 9.5px;
    margin-top: 3px;
  }

  .contact {
    font-family: "Open Sans", sans-serif;
    color: var(--white);
    font-size: 10px;
    line-height: 16px;
  }
  .card--front .contact {
    position: absolute;
    right: 41px; top: 106px;
    text-align: right;
  }
  .contact__phone { display: inline-flex; align-items: center; gap: 3px; }
  .contact__phone svg { width: 9px; height: 9px; }

  .spine {
    position: absolute;
    left: 46px; top: 120px;
    transform: translate(-50%, -50%) rotate(-90deg);
    white-space: nowrap;
    text-align: center;
    color: var(--ink);
    font-family: "Oswald", sans-serif;
    line-height: 11px;
  }
  .spine__name { font-weight: 600; font-size: 11.5px; }
  .spine__title { font-weight: 300; font-style: italic; font-size: 10.5px; }

  .bio {
    position: absolute;
    left: 339px; top: 45px;
    width: 166px;
    font-family: "Oswald", sans-serif;
    font-weight: 300;
    color: var(--white);
    font-size: 7.9px;
    line-height: 10.3px;
  }
  .bio p + p { margin-top: 6px; }
  .bio .contact {
    font-family: "Oswald", sans-serif;
    font-weight: 400;
    font-size: 8.6px;
    line-height: 10.5px;
    margin-top: 6px;
  }
</style>
</head>
<body>

<section class="card card--front" aria-label="Front of card">
  <svg class="card__shapes" viewBox="0 0 540 240" aria-hidden="true">
    <polygon points="160,0 204,0 204,240 150,240" fill="var(--cream)"/>
    <polygon points="3,12 170,2 158,230 0,224" fill="var(--tan)"/>
    <polygon points="363,0 540,6 540,240 363,240" fill="var(--grey-shadow)"/>
  </svg>
  <div class="photo" role="img" aria-label="Photo of Marcelo smiling, wearing a grey t-shirt and jeans"></div>
  <svg class="card__shapes" viewBox="0 0 540 240" aria-hidden="true">
    <polygon points="363,3 533,12 528,234 363,234" fill="var(--grey)"/>
  </svg>
  <div class="frame"></div>
  <div class="identity">
    <div class="identity__name">Marcelo Vantrini</div>
    <div class="identity__title">Tenor &amp; Vocal Coach</div>
  </div>
  <div class="contact">
    <div>mvbaritono@quellmail.net</div>
    <div class="contact__phone">
      <svg viewBox="0 0 10 10"><circle cx="5" cy="5" r="4.4" fill="none" stroke="currentColor" stroke-width="0.9"/><path d="M3.4 2.6c.4-.3.7-.2.9.2l.4.8c.1.3 0 .5-.2.6l-.3.2c.3.7.8 1.2 1.4 1.5l.2-.3c.2-.2.4-.3.7-.1l.7.4c.3.2.4.5.1.9l-.3.3c-.5.4-2 0-3-1s-1.4-2.5-1-3z" fill="currentColor"/></svg>
      (713) 562-8307
    </div>
  </div>
</section>

<section class="card card--back" aria-label="Back of card">
  <svg class="card__shapes" viewBox="0 0 540 240" aria-hidden="true">
    <polygon points="2,4 81,12 81,236 5,236" fill="var(--tan)"/>
    <polygon points="382,0 540,0 540,240 374,240" fill="var(--grey)"/>
  </svg>
  <div class="photo" role="img" aria-label="Portrait of Marcelo in a dark jacket and open white shirt"></div>
  <div class="spine">
    <div class="spine__name">Marcelo Vantrini</div>
    <div class="spine__title">Tenor &amp; Vocal Coach</div>
  </div>
  <div class="bio">
    <p>Marcelo is a local singer and actor who has been working professionally around the country as a concert artist and musical theater performer. He studied at the Halvern School of Music, Bayline University and works as a vocal coach with local youths and adults in the Houston area. Marcelo's goal is to help his students master their individual instrument so that they can achieve a natural and effortless vocal production.</p>
    <p>For more information please<br>contact Marcelo today!</p>
    <div class="contact">
      <div>mvbaritono@quellmail.net</div>
      <div class="contact__phone">
        <svg viewBox="0 0 10 10"><circle cx="5" cy="5" r="4.4" fill="none" stroke="currentColor" stroke-width="0.9"/><path d="M3.4 2.6c.4-.3.7-.2.9.2l.4.8c.1.3 0 .5-.2.6l-.3.2c.3.7.8 1.2 1.4 1.5l.2-.3c.2-.2.4-.3.7-.1l.7.4c.3.2.4.5.1.9l-.3.3c-.5.4-2 0-3-1s-1.4-2.5-1-3z" fill="currentColor"/></svg>
        (713) 562-8307
      </div>
    </div>
  </div>
</section>

</body>
</html>
```